Geek Pagoda home page design

I'd like to take quirkvault.com existing home page and use the logo attached and make and the home page look like brainbazaar.com home page or foreverimp.com. The font size of the buttons should be similar to brainbazaar.com. does this make sense?
I've added a mock up of the layout design. I'm looking for fun nerd like design on the left and right of the borders. It should be faint but visible and add more character to the site apart from just a solid black thick border. We'd like the Glasses to be a Favicon as well.
Getting better. Let's try the logo in the top middle of the page and make sure it is bigger than the banner to the left and right. Add maybe the search bar to the left and the shipping info to the right of the log pyramid. if you do this right the pyramid will look like a nose and the surrounding rectangles will look like the glasses inside the logo we have.
Can you make the robots look like the orbit cinema gallery robots? They were the shadows of three robots at the bottom right of the tv show and they were watching movies and commenting on them. It may be a nice touch to have the robots looking at the site instead of at us the shopper from the bottom right.
Can you experiment with the side columns with what the inside of a temple may look like. Maybe some Egyptian columns with torches hanging from them.
Also can we try less pastel colors and more bold primary colors. Maybe experiment with Orange or a darker bolder blue?
Nice work. Also please correct spelling of "Customer" in the bar. And can you add a Q Roll feature in the middle above the products? this is where five featured products will rotate like a QRoll works
Updates
Project Deadline Extended
Reason: We have the holiday coming up and I guaranteed payment so we would like to see some quality work.
Target Market(s)
Target Market is young Moms, College Students and kids
Industry/Entity Type
Shipping
Look and feel
Each slider illustrates characteristics of the customer's brand and the style your logo design should communicate.

```html
<!DOCTYPE html>
<html lang="en">
<head>
<meta charset="utf-8">
<title>Geek Pagoda</title>
<link rel="stylesheet" href="https://fonts.googleapis.com/css2?family=Didact+Gothic&family=Open+Sans:wght@400;600&display=swap">
<style>
:root{
  --orange:#fb8c13;
  --orange-dark:#e2700a;
  --price:#f26a10;
  --ink:#222;
  --line:#d9d9d9;
  --panel:#f3f3f3;
  --page:#ececec;
  --black:#000;
  --white:#fff;
  --red:#e8302f;
  --green:#6fd51c;
  --blue:#2455d6;
  --purple:#8a4fc7;
  --pink:#ea4fb8;
  --yellow:#f4cf1c;
  --mint:#a9d6a4;
  --aqua:#9fd3df;
}
*{box-sizing:border-box;margin:0;padding:0}
html,body{width:973px;height:1200px;overflow:hidden}
body{background:var(--page);font-family:"Didact Gothic",sans-serif;color:var(--ink);position:relative}
.sheet{position:absolute;left:11px;top:0;width:956px;height:1128px;background:var(--white)}
.abs{position:absolute}
.topbar{left:0;top:0;width:956px;height:28px;background:#efefef;font:12px "Open Sans",sans-serif;color:#444;text-align:right;padding:7px 58px 0 0}
.topbar span{margin:0 8px;color:#999}
.brand{left:56px;top:74px;display:flex;align-items:center;gap:10px;font-size:28px;color:var(--black)}
.brand i{display:block;width:22px;height:22px;background:var(--black)}
.quick{top:66px;width:98px;text-align:center;font:12px "Open Sans",sans-serif;color:#555}
.quick svg{display:block;margin:0 auto}
.quick .btn{display:block;margin-top:8px;background:#eee;border-radius:6px;height:22px;line-height:22px}
.nav{left:0;top:171px;width:956px;height:36px;background:var(--orange);display:flex;font:600 13px "Open Sans",sans-serif;color:var(--white)}
.nav a{display:block;text-align:center;line-height:36px;border-right:1px solid rgba(255,255,255,.35);text-decoration:none;color:inherit}
.nav a.current{background:var(--orange-dark)}
.box{border:1px solid var(--line);background:var(--panel)}
.box h2{font-weight:400;font-size:16px;color:var(--black)}
.search{left:4px;top:216px;width:189px;height:76px;padding:10px 14px}
.search .field{position:absolute;left:11px;top:33px;width:140px;height:18px;background:var(--white);border:1px solid #ddd}
.search .go{position:absolute;left:147px;top:28px;width:28px;height:28px;border-radius:50%;background:var(--orange);color:var(--white);font-size:12px;text-align:center;line-height:28px}
.cats{left:4px;top:296px;width:189px;height:252px;padding:8px 14px}
.cats ul{list-style:none;margin-top:10px;font-size:12px}
.cats li{height:21px;line-height:20px;border-bottom:1px solid #e4e4e4;padding-left:18px;position:relative;width:158px}
.cats li::before{content:"";position:absolute;left:4px;top:7px;border:3px solid transparent;border-left:4px solid #aaa}
.news{left:4px;top:553px;width:189px;height:141px;padding:10px 10px}
.news .in{height:22px;margin-top:10px;background:var(--white);border:1px solid #ccc;border-radius:10px;font-size:10px;font-style:italic;color:#888;padding:4px 10px}
.news .sub{position:absolute;right:8px;top:102px;background:var(--orange-dark);color:var(--white);font:12px "Open Sans",sans-serif;padding:4px 11px;border-radius:4px}
.videos{left:4px;top:701px;width:189px;height:427px;padding:10px 12px;background:var(--white)}
.videos .player{position:absolute;left:8px;top:36px;width:174px;height:110px;background:var(--black)}
.hero{left:201px;top:218px;width:541px;height:275px;border:1px solid var(--line);padding:3px;background:var(--white)}
.hero .photo{width:100%;height:100%;
  background:
    radial-gradient(ellipse 70px 80px at 40% 62%,var(--green),transparent 70%),
    radial-gradient(ellipse 60px 70px at 37% 25%,var(--red),transparent 70%),
    radial-gradient(ellipse 90px 60px at 62% 22%,var(--purple),transparent 70%),
    radial-gradient(ellipse 60px 80px at 74% 60%,var(--blue),transparent 70%),
    radial-gradient(ellipse 70px 60px at 58% 72%,#f0701c,transparent 70%),
    radial-gradient(ellipse 50px 50px at 52% 48%,var(--pink),transparent 70%),
    radial-gradient(ellipse 50px 60px at 16% 75%,#d6d6d6,transparent 70%),
    var(--white)}
.jokes{left:748px;top:216px;width:194px;height:278px;padding:7px 10px;background:var(--white)}
.jokes h2{font-size:16px}
.note{position:absolute;left:1px;width:190px;height:74px;background:var(--panel);border-bottom:1px solid #ddd;padding:6px 4px 0 60px;font:10px/15px "Open Sans",sans-serif;color:#444}
.note .thumb{position:absolute;left:7px;top:10px;width:48px;height:42px;background:radial-gradient(circle at 40% 50%,#f58b1d,#2d5fcf 60%,var(--white) 90%)}
.note b{font-weight:400;display:block;margin-top:4px;color:#111}
.viewall{position:absolute;left:7px;top:266px;width:190px;height:13px;border-radius:6px;background:var(--orange);color:var(--white);font-size:10px;text-align:right;padding-right:12px;line-height:13px}
.newbar{left:200px;top:500px;width:743px;height:30px;background:linear-gradient(#333,#000);border-radius:4px 4px 0 0;color:var(--white);font-size:17px;padding:4px 14px}
.card{position:absolute;width:170px;height:186px;border:1px solid #ddd;background:var(--white);padding:10px 9px}
.card .pic{height:100px;background-color:#f4f4f4}
.card h3{font-weight:400;font-size:13px;color:#444;margin-top:12px;letter-spacing:.3px}
.card p{font-size:13px;margin-top:5px}
.card p em{font-style:normal;color:var(--price);margin-right:5px}
.card .add{display:inline-block;margin-top:6px;background:var(--black);color:var(--white);font:12px "Open Sans",sans-serif;padding:2px 10px}
.shapes{height:46px!important;background:
  radial-gradient(ellipse 12px 18px at 10% 55%,var(--red),transparent 75%),
  radial-gradient(ellipse 14px 16px at 27% 55%,#f07a1a,transparent 75%),
  radial-gradient(ellipse 10px 18px at 43% 55%,var(--yellow),transparent 75%),
  radial-gradient(circle 13px at 60% 60%,var(--green),transparent 75%),
  radial-gradient(ellipse 12px 16px at 77% 60%,#24a9e2,transparent 75%),
  radial-gradient(ellipse 12px 18px at 92% 60%,var(--purple),transparent 75%),#f4f4f4}
.pack{background:
  radial-gradient(circle 24px at 20% 60%,var(--red),transparent 75%),
  radial-gradient(circle 24px at 50% 58%,var(--yellow),transparent 75%),
  radial-gradient(circle 24px at 80% 48%,#3b6ed6,transparent 75%),
  linear-gradient(#d8d8d8,#c9ccd0)}
.pack-b{background:
  radial-gradient(circle 22px at 22% 60%,var(--yellow),transparent 75%),
  radial-gradient(circle 22px at 50% 58%,#222,transparent 75%),
  radial-gradient(circle 22px at 80% 50%,#f2f2f2,transparent 75%),
  linear-gradient(#d8d8d8,#c9ccd0)}
.men{background:
  radial-gradient(ellipse 45px 50px at 35% 55%,var(--mint),transparent 75%),
  radial-gradient(ellipse 40px 50px at 68% 45%,var(--aqua),transparent 75%),#eef0ee}
.crowd{background:
  radial-gradient(ellipse 20px 30px at 12% 55%,var(--red),transparent 75%),
  radial-gradient(ellipse 20px 30px at 30% 55%,#f2a322,transparent 75%),
  radial-gradient(ellipse 20px 30px at 48% 55%,var(--pink),transparent 75%),
  radial-gradient(ellipse 20px 30px at 66% 55%,var(--green),transparent 75%),
  radial-gradient(ellipse 20px 30px at 86% 55%,var(--blue),transparent 75%),#f1f1f1}
.dark{background:
  radial-gradient(ellipse 40px 40px at 45% 45%,#1a1a1a,transparent 75%),
  radial-gradient(ellipse 35px 25px at 85% 85%,#e11,transparent 75%),#f1f1f1}
.footer{left:0;top:1128px;width:973px;height:50px;background:#f2f2f2;font:11px "Open Sans",sans-serif;color:#444}
.footer .copy{position:absolute;left:21px;top:18px}
.footer .links{position:absolute;right:20px;top:20px}
.footer .links span{margin:0 9px;color:#888}
</style>
</head>
<body>
<div class="sheet">
  <div class="abs topbar">Order Status<span>|</span>Gift Certificates<span>|</span>Sign in or Create an account</div>
  <div class="abs brand"><i></i>Geek Pagoda</div>
  <div class="abs quick" style="left:711px">
    <svg width="40" height="40" viewBox="0 0 40 40"><circle cx="20" cy="12" r="9" fill="#111"/><path d="M3 38c0-12 8-16 17-16s17 4 17 16z" fill="#111"/></svg>
    <span class="btn">My Account</span>
  </div>
  <div class="abs quick" style="left:818px">
    <svg width="44" height="40" viewBox="0 0 44 40"><rect x="3" y="6" width="38" height="30" rx="3" fill="#111"/><rect x="8" y="14" width="10" height="10" fill="#fff"/><rect x="22" y="14" width="14" height="3" fill="#fff"/><rect x="22" y="21" width="14" height="3" fill="#fff"/><rect x="14" y="2" width="4" height="7" fill="#111"/><rect x="26" y="2" width="4" height="7" fill="#111"/></svg>
    <span class="btn">View Cart</span>
  </div>
  <nav class="abs nav"><a class="current" style="width:98px">HOME</a><a style="width:176px">SHIPPING &amp; RETURNS</a><a style="width:160px">RSS SYNDICATION</a><a style="width:85px">ORDER</a><a style="width:120px;border:0">WISH LIST</a></nav>

  <section class="abs box search"><h2>Search</h2><div class="field"></div><div class="go">go</div></section>
  <section class="abs box cats"><h2>Categories</h2>
    <ul><li>Candles</li><li>Decor</li><li>Key Covers</li><li>Kitchen</li><li>Magnets</li><li>Office</li><li>Toys</li><li>Candles</li><li>Decor</li><li style="border:0">Key Covers</li></ul>
  </section>
  <section class="abs box news"><h2>Newsletter Sign Up</h2>
    <div class="in">First name</div><div class="in">email address</div><span class="sub">SUBSCRIBE ME</span>
  </section>
  <section class="abs box videos"><h2>Latest Videos</h2>
    <div class="player"><svg class="abs" style="left:80px;top:46px" width="18" height="20" viewBox="0 0 18 20"><path d="M0 0l18 10L0 20z" fill="#fff"/></svg></div>
  </section>

  <div class="abs hero"><div class="photo" role="img" aria-label="Colourful bendy magnetic figures linked in a ring"></div></div>

  <section class="abs box jokes"><h2>Jokes &amp; Announcments</h2>
    <div class="note" style="top:34px"><div class="thumb" role="img" aria-label="Announcement photo"></div>Brightloop Studio to specialize in advanced projects and ongoing.<b>READ MORE</b></div>
    <div class="note" style="top:110px"><div class="thumb" role="img" aria-label="Announcement photo"></div>Brightloop Studio to specialize in advanced projects and ongoing.<b>READ MORE</b></div>
    <div class="note" style="top:186px;border:0"><div class="thumb" role="img" aria-label="Announcement photo"></div>Brightloop Studio to specialize in advanced projects and ongoing.<b>READ MORE</b></div>
    <div class="viewall" style="width:180px">view all</div>
  </section>

  <div class="abs newbar">New Products</div>

  <article class="card" style="left:208px;top:536px"><div class="pic shapes" role="img" aria-label="Coloured geometric magnet shapes"></div><h3 style="margin-top:64px">Geomagnetic Shaps</h3><p><em>$10.75</em>Not Rated</p><span class="add">Add to cart</span></article>
  <article class="card" style="left:392px;top:536px"><div class="pic pack" role="img" aria-label="Packaged emoji key covers"></div><h3>Geomagnetic Shaps</h3><p><em>$10.75</em>Not Rated</p><span class="add">Add to cart</span></article>
  <article class="card" style="left:582px;top:536px"><div class="pic pack-b" role="img" aria-label="Packaged animal key covers"></div><h3>Geomagnetic Shaps</h3><p><em>$10.75</em>Not Rated</p><span class="add">Add to cart</span></article>
  <article class="card" style="left:763px;top:536px"><div class="pic men" role="img" aria-label="Translucent bendy magnet figures"></div><h3>Geomagnetic Shaps</h3><p><em>$10.75</em>Not Rated</p><span class="add">Add to cart</span></article>

  <article class="card" style="left:208px;top:732px"><div class="pic crowd" style="height:72px" role="img" aria-label="Row of colourful magnet figures"></div><h3 style="margin-top:38px">Geomagnetic Shaps</h3><p><em>$10.75</em>Not Rated</p><span class="add">Add to cart</span></article>
  <article class="card" style="left:392px;top:732px"><div class="pic crowd" style="height:80px" role="img" aria-label="Colourful magnet figures linking arms"></div><h3 style="margin-top:34px">Geomagnetic Shaps</h3><p><em>$10.75</em>Not Rated</p><span class="add">Add to cart</span></article>
  <article class="card" style="left:582px;top:732px"><div class="pic crowd" style="height:72px" role="img" aria-label="Row of colourful magnet figures"></div><h3 style="margin-top:38px">Geomagnetic Shaps</h3><p><em>$10.75</em>Not Rated</p><span class="add">Add to cart</span></article>
  <article class="card" style="left:763px;top:732px"><div class="pic dark" role="img" aria-label="Black magnet figure on a red figure"></div><h3>Geomagnetic Shaps</h3><p><em>$10.75</em>Not Rated</p><span class="add">Add to cart</span></article>

  <article class="card" style="left:208px;top:927px"><div class="pic crowd" style="height:72px" role="img" aria-label="Row of colourful magnet figures"></div><h3 style="margin-top:34px">Geomagnetic Shaps</h3><p><em>$10.75</em>Not Rated</p><span class="add">Add to cart</span></article>
  <article class="card" style="left:392px;top:927px"><div class="pic pack" style="height:94px" role="img" aria-label="Packaged emoji key covers"></div><h3>Geomagnetic Shaps</h3><p><em>$10.75</em>Not Rated</p><span class="add">Add to cart</span></article>
  <article class="card" style="left:582px;top:927px"><div class="pic shapes" role="img" aria-label="Coloured geometric magnet shapes"></div><h3 style="margin-top:70px">Geomagnetic Shaps</h3><p><em>$10.75</em>Not Rated</p><span class="add">Add to cart</span></article>
  <article class="card" style="left:763px;top:927px"><div class="pic men" role="img" aria-label="Translucent bendy magnet figures"></div><h3>Geomagnetic Shaps</h3><p><em>$10.75</em>Not Rated</p><span class="add">Add to cart</span></article>
</div>
<footer class="abs footer">
  <div class="copy">© 2012 Company Name &nbsp;|&nbsp; All right reserved</div>
  <div class="links">HOME<span>|</span>SHIPPING &amp; RETURNS<span>|</span>RSS SYNDICATION<span>|</span>ORDER<span>|</span>WISH LIST</div>
</footer>
</body>
</html>
```